Create a new business card

I’m looking to update my business card to make it match the rest of my brand. I will include my current website as well as what my vehicle designs look like, etc..
What my business currently services
Weekly maintenance pool openings / closings
Equipment repair, including pumps, heaters, salt systems, filters, etc.
We install automatic covers and maintain them as well as provide preventative maintenance

I would like to include my name.
Darren Holcott.
My title
Owner
My email
Darren@tidewellnx.com
4015867120
Www.tidewellnx.com

```html
<!DOCTYPE html>
<html lang="en">
<head>
<meta charset="utf-8">
<title>Tidewell Pool Service – Business Card</title>
<link href="https://fonts.googleapis.com/css2?family=Oswald:wght@300;400;500&display=swap" rel="stylesheet">
<style>
  :root {
    --navy: #1d2c5e;
    --aqua: #27b4e8;
    --orange: #e5632a;
    --white: #ffffff;
    --backdrop: #2b2b2d;
  }
  html, body { margin: 0; padding: 0; overflow: hidden; }
  body {
    width: 1200px; height: 962px;
    background: var(--backdrop);
    font-family: "Oswald", sans-serif;
    position: relative;
  }
  .card {
    position: absolute;
    left: 280px;
    width: 640px; height: 366px;
    border-radius: 18px;
    overflow: hidden;
  }
  .card-back { top: 88px; background: var(--navy); }
  .card-front { top: 508px; background: var(--white); }

  .brand {
    position: absolute;
    display: flex; align-items: center; gap: 12px;
  }
  .brand-dot { width: 30px; height: 30px; border-radius: 50%; background: var(--aqua); flex: none; }
  .brand-name {
    font-weight: 500; font-size: 30px; line-height: 1.05;
    text-transform: uppercase; letter-spacing: 1px;
  }
  .card-back .brand { left: 52px; top: 140px; }
  .card-back .brand-name { color: var(--white); }
  .card-front .brand { left: 48px; top: 70px; }
  .card-front .brand-name { color: var(--navy); }

  .services {
    position: absolute; left: 340px; top: 52px;
    list-style: none; margin: 0; padding: 0;
  }
  .services li {
    display: flex; align-items: center; gap: 9px;
    color: var(--white); font-weight: 300; font-size: 15.5px;
    text-transform: uppercase; letter-spacing: .5px; line-height: 21.5px;
  }
  .tick { width: 13px; height: 13px; flex: none; }

  .swoosh { position: absolute; left: 0; top: 0; }

  .contact {
    position: absolute; right: 36px; top: 158px;
    text-align: right; text-transform: uppercase;
  }
  .contact-name { color: var(--aqua); font-weight: 500; font-size: 30px; line-height: 1; letter-spacing: .5px; }
  .contact-title { color: var(--orange); font-weight: 400; font-size: 17px; margin-top: 4px; }
  .contact-row {
    display: flex; justify-content: flex-end; align-items: center; gap: 10px;
    color: var(--white); font-weight: 300; font-size: 16px; margin-top: 6px;
  }
  .contact-row.phone { font-size: 20px; font-weight: 400; margin-top: 8px; }
  .icon { width: 16px; height: 16px; flex: none; }
</style>
</head>
<body>

<section class="card card-back">
  <div class="brand">
    <span class="brand-dot"></span>
    <span class="brand-name">Tidewell<br>Pool Service</span>
  </div>
  <ul class="services">
    <li><svg class="tick" viewBox="0 0 14 14"><circle cx="7" cy="7" r="7" fill="#e5632a"/><path d="M3.8 7.2l2.2 2.1 4.2-4.4" stroke="#fff" stroke-width="1.8" fill="none"/></svg>Weekly pool maintenance</li>
    <li><svg class="tick" viewBox="0 0 14 14"><circle cx="7" cy="7" r="7" fill="#e5632a"/><path d="M3.8 7.2l2.2 2.1 4.2-4.4" stroke="#fff" stroke-width="1.8" fill="none"/></svg>Pool opening &amp; closing</li>
    <li><svg class="tick" viewBox="0 0 14 14"><circle cx="7" cy="7" r="7" fill="#e5632a"/><path d="M3.8 7.2l2.2 2.1 4.2-4.4" stroke="#fff" stroke-width="1.8" fill="none"/></svg>Equipment servicing</li>
    <li><svg class="tick" viewBox="0 0 14 14"><circle cx="7" cy="7" r="7" fill="#e5632a"/><path d="M3.8 7.2l2.2 2.1 4.2-4.4" stroke="#fff" stroke-width="1.8" fill="none"/></svg>Equipment installation</li>
    <li><svg class="tick" viewBox="0 0 14 14"><circle cx="7" cy="7" r="7" fill="#e5632a"/><path d="M3.8 7.2l2.2 2.1 4.2-4.4" stroke="#fff" stroke-width="1.8" fill="none"/></svg>Structural pool repair</li>
    <li><svg class="tick" viewBox="0 0 14 14"><circle cx="7" cy="7" r="7" fill="#e5632a"/><path d="M3.8 7.2l2.2 2.1 4.2-4.4" stroke="#fff" stroke-width="1.8" fill="none"/></svg>Plumbing updates &amp; upgrades</li>
    <li><svg class="tick" viewBox="0 0 14 14"><circle cx="7" cy="7" r="7" fill="#e5632a"/><path d="M3.8 7.2l2.2 2.1 4.2-4.4" stroke="#fff" stroke-width="1.8" fill="none"/></svg>Coping replacement &amp; removal</li>
    <li><svg class="tick" viewBox="0 0 14 14"><circle cx="7" cy="7" r="7" fill="#e5632a"/><path d="M3.8 7.2l2.2 2.1 4.2-4.4" stroke="#fff" stroke-width="1.8" fill="none"/></svg>Tile replacement &amp; removal</li>
    <li><svg class="tick" viewBox="0 0 14 14"><circle cx="7" cy="7" r="7" fill="#e5632a"/><path d="M3.8 7.2l2.2 2.1 4.2-4.4" stroke="#fff" stroke-width="1.8" fill="none"/></svg>Interior resurfacing/replastering</li>
    <li><svg class="tick" viewBox="0 0 14 14"><circle cx="7" cy="7" r="7" fill="#e5632a"/><path d="M3.8 7.2l2.2 2.1 4.2-4.4" stroke="#fff" stroke-width="1.8" fill="none"/></svg>Filter system equipment upgrades</li>
    <li><svg class="tick" viewBox="0 0 14 14"><circle cx="7" cy="7" r="7" fill="#e5632a"/><path d="M3.8 7.2l2.2 2.1 4.2-4.4" stroke="#fff" stroke-width="1.8" fill="none"/></svg>Decking removal &amp; renovation</li>
    <li><svg class="tick" viewBox="0 0 14 14"><circle cx="7" cy="7" r="7" fill="#e5632a"/><path d="M3.8 7.2l2.2 2.1 4.2-4.4" stroke="#fff" stroke-width="1.8" fill="none"/></svg>Commercial pool services</li>
  </ul>
</section>

<section class="card card-front">
  <svg class="swoosh" width="640" height="366" viewBox="0 0 640 366" aria-hidden="true">
    <path d="M232 366 C237 185 372 72 590 56 C630 53 640 70 640 80 L640 366 Z" fill="#e5632a"/>
    <path d="M242 366 C247 190 380 80 592 66 C628 64 640 80 640 92 L640 366 Z" fill="#ffffff"/>
    <path d="M250 366 C254 192 386 86 594 74 C632 72 640 100 640 120 L640 366 Z" fill="#27b4e8"/>
    <path d="M270 366 C275 198 400 100 598 88 C626 87 638 105 640 125 L640 366 Z" fill="#ffffff"/>
    <path d="M280 366 C285 200 410 105 600 95 C626 94 638 112 640 132 L640 366 Z" fill="#1d2c5e"/>
  </svg>

  <div class="brand">
    <span class="brand-dot"></span>
    <span class="brand-name">Tidewell<br>Pool Service</span>
  </div>

  <div class="contact">
    <div class="contact-name">Darren Holcott</div>
    <div class="contact-title">Owner</div>
    <div class="contact-row phone">(401) 586-7120
      <svg class="icon" viewBox="0 0 16 16"><path d="M4 1.5l2.4 3-1.3 1.6c.8 1.9 2.3 3.4 4.2 4.2l1.6-1.3 3 2.4-1.4 2.5C7.2 13.8 2.2 8.8 1.6 3z" fill="#27b4e8"/></svg>
    </div>
    <div class="contact-row">Darren@tidewellnx.com
      <svg class="icon" viewBox="0 0 16 16"><rect x="1" y="3" width="14" height="10" fill="#27b4e8"/><path d="M1 3l7 6 7-6" stroke="#1d2c5e" stroke-width="1.3" fill="none"/></svg>
    </div>
    <div class="contact-row">tidewellnx.com
      <svg class="icon" viewBox="0 0 16 16"><circle cx="8" cy="8" r="7" fill="#27b4e8"/><path d="M1 8h14M8 1c-3 3.5-3 10.5 0 14M8 1c3 3.5 3 10.5 0 14" stroke="#1d2c5e" stroke-width="1" fill="none"/></svg>
    </div>
  </div>
</section>

</body>
</html>
```